Letterhead and Business Cards

Using our new logo we would like designs for the following,

1.Letterhead

2. 2 x Business Cards

I will need all three in high quality PDF files ready for printing. I will also require the top and bottom of the letterhead as two JPG files.

Target Market(s)

We are a business to business company dealing with middle to upper management both as clients and suppliers.

Industry/Entity Type

Business

Requirements
Must have
• 1. Look professional.
• 2. Utilise our logo colours
• 3. Incorporate our logo on both.
• 4. Letterhead

• Address:
• Kelmont Yard House
• Kelmont Yard Lane
• London
• SE9 4TQ

• Tel:0845 312 4096
• Fax: 0845 312 7041
• Website: www.quillomarket.example
• Email: info@quillomarket.example

• Directors: G.H. Pomfrey and M.R. Pomfrey Company Registration No: 52640918(This should be quite small in the letterhead footer somewhere)

• Business Card One Sided Only

• 1. Gideon H. Pomfrey
• Managing Director

• Address:
• Kelmont Yard House
• Kelmont Yard Lane
• London
• SE9 4TQ

• Tel:0845 312 4096
• Fax: 0845 312 7042
• Mob: 0791 563 2208
• Email: gideon@quillomarket.example

• 2. Miriam R. Pomfrey
• Sales Director

• Address:
• Kelmont Yard House
• Kelmont Yard Lane
• London
• SE9 4TQ

• Tel:0845 312 4096
• Fax: 0845 312 7041
• Mob: 0794 826 1159
• Email: miriam@quillomarket.example

• Please note some of this info may change for final printing.

```html
<!DOCTYPE html>
<html lang="en">
<head>
<meta charset="utf-8">
<title>Quillo Market Letterhead</title>
<link href="https://fonts.googleapis.com/css2?family=Lato:wght@400;700&display=swap" rel="stylesheet">
<style>
  :root {
    --brand-green: #9bc93b;
    --brand-grey: #8c8c8c;
    --ink: #1f1f1f;
    --muted: #858585;
    --paper: #ffffff;
    --paper-shade: #e9e9e9;
  }
  * { margin: 0; padding: 0; box-sizing: border-box; }
  html, body { width: 848px; height: 1200px; overflow: hidden; }
  body { font-family: "Lato", "Gill Sans", sans-serif; background: var(--paper); }

  .letterhead {
    position: relative;
    width: 848px;
    height: 1200px;
    background: linear-gradient(to bottom, var(--paper) 0, var(--paper) 600px, var(--paper-shade) 1200px);
    overflow: hidden;
  }
  .side-band {
    position: absolute;
    left: 0; top: 0;
    width: 37px; height: 100%;
    background: var(--brand-green);
  }

  .brand {
    position: absolute;
    top: 40px;
    right: 44px;
    display: flex;
    flex-direction: column;
    align-items: center;
    gap: 14px;
  }
  .brand-mark {
    width: 118px; height: 118px;
    border-radius: 50%;
    background: var(--brand-green);
  }
  .brand-name {
    font-size: 36px;
    font-weight: 700;
    color: var(--brand-grey);
    letter-spacing: -0.5px;
    line-height: 1;
  }

  .contact {
    position: absolute;
    right: 41px;
    top: 1126px;
    text-align: right;
  }
  .contact-address {
    font-size: 15.5px;
    color: var(--ink);
    line-height: 20px;
  }
  .contact-online {
    font-size: 15px;
    color: var(--muted);
    line-height: 20px;
  }

  .legal-band {
    position: absolute;
    left: 333px; right: 0;
    bottom: 0;
    height: 23px;
    background: var(--brand-green);
    color: var(--paper);
    font-size: 10px;
    line-height: 23px;
    text-align: right;
    padding-right: 39px;
  }
</style>
</head>
<body>
  <main class="letterhead">
    <div class="side-band"></div>

    <header class="brand">
      <span class="brand-mark"></span>
      <span class="brand-name">Quillo Market</span>
    </header>

    <footer class="contact">
      <p class="contact-address">Kelmont Yard House, Kelmont Yard Lane, London, SE9 4TQ</p>
      <p class="contact-online">www.quillomarket.example | info@quillomarket.example</p>
    </footer>

    <div class="legal-band">Directors: G.H. Pomfrey and M.R. Pomfrey Company Registration No: 52640918</div>
  </main>
</body>
</html>
```